Lantern Business Cards

Need business cards for my employees at my restaurant.

Needs to include:
Our Logo
Lantern Bowls & Brews
Name: Nora Pettigrew
Title : Owner
Address: 487 Mirella Ave. Lake Havasu City, AZ 86519
Web: www.lanternkestrel.com
Phone: 928-555-0147
Cell: 928-555-0192
Email: info@lanternkestrel.com

```html
<!DOCTYPE html>
<html lang="en">
<head>
<meta charset="utf-8">
<title>Lantern Business Cards</title>
<link rel="stylesheet" href="https://fonts.googleapis.com/css2?family=Lexend:wght@500;600;700&family=Heebo:wght@400;500&display=swap">
<style>
  :root{
    --red:#c1232f;
    --red-bright:#f92432;
    --black:#0b0b0c;
    --charcoal:#252525;
    --ink:#111111;
    --paper:#ffffff;
    --bg:#e9e9e9;
  }
  html,body{margin:0;padding:0;}
  body{width:1047px;height:1200px;overflow:hidden;background:var(--bg);position:relative;}
  .card{
    position:absolute;left:65px;width:1050px;height:600px;
    transform:scale(.8725);transform-origin:0 0;
    background:var(--paper);border-radius:44px;overflow:hidden;
    box-shadow:0 8px 28px rgba(0,0,0,.28);
  }
  .card--front{top:37px;}
  .card--back{top:624px;}
  .card__art{position:absolute;inset:0;width:1050px;height:600px;}
  .person{position:absolute;left:67px;top:62px;width:320px;}
  .person__name{
    font-family:"Lexend",sans-serif;font-weight:500;font-size:57px;line-height:1;
    color:var(--red);margin:0;white-space:nowrap;letter-spacing:-.5px;
  }
  .person__title{
    font-family:"Lexend",sans-serif;font-weight:500;font-size:31px;color:var(--ink);
    text-align:right;margin:10px 0 0;line-height:1;
  }
  .person__rule{height:3px;background:var(--red);margin-top:12px;}
  .contact{
    position:absolute;left:88px;top:342px;margin:0;padding:0;list-style:none;
    font-family:"Heebo",sans-serif;font-size:27px;color:var(--ink);line-height:34px;
  }
  .contact li{display:flex;align-items:flex-start;margin-bottom:10px;}
  .contact li.tight{margin-bottom:4px;}
  .contact svg{width:30px;height:30px;flex:none;margin:2px 24px 0 0;fill:var(--red);}
  .brand{
    position:absolute;left:290px;right:0;top:120px;text-align:center;
  }
  .brand__mark{width:150px;height:150px;border-radius:50%;background:var(--red);margin:0 auto 34px;}
  .brand__name{
    font-family:"Lexend",sans-serif;font-weight:700;font-size:52px;line-height:1;
    color:var(--red);margin:0;white-space:nowrap;
  }
</style>
</head>
<body>

<section class="card card--front" aria-label="Business card front">
  <svg class="card__art" viewBox="0 0 1050 600" aria-hidden="true">
    <polygon fill="var(--red)" points="885,273 1050,375 1050,600 915,600 745,488"/>
    <polygon fill="var(--red-bright)" points="953,318 1050,378 1050,583 1043,583 860,471"/>
    <polygon fill="var(--black)" points="870,0 1050,0 1050,373 755,190"/>
    <polygon fill="var(--charcoal)" points="965,0 1050,0 1050,278 870,163"/>
  </svg>

  <div class="person">
    <h1 class="person__name">Nora Pettigrew</h1>
    <p class="person__title">Owner</p>
    <div class="person__rule"></div>
  </div>

  <ul class="contact">
    <li><svg viewBox="0 0 24 24"><path d="M12 2a7 7 0 0 0-7 7c0 5 7 13 7 13s7-8 7-13a7 7 0 0 0-7-7zm0 9.5A2.5 2.5 0 1 1 12 6.5a2.5 2.5 0 0 1 0 5z"/></svg><span>487 Mirella Ave. Lake<br>Havasu City, AZ 86519</span></li>
    <li><svg viewBox="0 0 24 24"><path d="M12 3a9 9 0 1 0 0 18 9 9 0 0 0 0-18zm6.9 8h-3a14 14 0 0 0-1.2-5.3A7 7 0 0 1 18.9 11zM12 5c.9 1.2 1.7 3.4 1.9 6h-3.8c.2-2.6 1-4.8 1.9-6zM9.3 5.7A14 14 0 0 0 8.1 11h-3a7 7 0 0 1 4.2-5.3zM5.1 13h3a14 14 0 0 0 1.2 5.3A7 7 0 0 1 5.1 13zm6.9 6c-.9-1.2-1.7-3.4-1.9-6h3.8c-.2 2.6-1 4.8-1.9 6zm2.7-.7a14 14 0 0 0 1.2-5.3h3a7 7 0 0 1-4.2 5.3z"/></svg><span>www.lanternkestrel.com</span></li>
    <li class="tight"><svg viewBox="0 0 24 24"><path d="M6.6 10.8a15 15 0 0 0 6.6 6.6l2.2-2.2a1 1 0 0 1 1-.25 11.4 11.4 0 0 0 3.6.57 1 1 0 0 1 1 1V20a1 1 0 0 1-1 1A17 17 0 0 1 3 4a1 1 0 0 1 1-1h3.5a1 1 0 0 1 1 1c0 1.25.2 2.45.57 3.57a1 1 0 0 1-.25 1z"/></svg><span>928-555-0147</span></li>
    <li><svg viewBox="0 0 24 24"><path d="M8 1h8a2 2 0 0 1 2 2v18a2 2 0 0 1-2 2H8a2 2 0 0 1-2-2V3a2 2 0 0 1 2-2zm0 3v15h8V4zm3 16v1.5h2V20z"/></svg><span>928-555-0192</span></li>
    <li><svg viewBox="0 0 24 24"><path d="M2 5h20v14H2zm2 2v.6l8 5.6 8-5.6V7zm16 3-8 5.6L4 10v7h16z"/></svg><span>info@lanternkestrel.com</span></li>
  </ul>
</section>

<section class="card card--back" aria-label="Business card back">
  <svg class="card__art" viewBox="0 0 1050 600" aria-hidden="true">
    <polygon fill="var(--red)" points="165,273 303,490 135,600 0,600 0,375"/>
    <polygon fill="var(--red-bright)" points="95,318 190,468 10,577 0,575 0,375"/>
    <polygon fill="var(--black)" points="0,0 175,0 295,188 0,375"/>
    <polygon fill="var(--charcoal)" points="0,0 80,0 180,163 0,275"/>
  </svg>

  <div class="brand">
    <div class="brand__mark"></div>
    <p class="brand__name">Lantern Bowls &amp; Brews</p>
  </div>
</section>

</body>
</html>
```